Restaurant needs a vertical banner for fried catfish

Our restaurant is looking for an eye-catching 78.75in. x 36in. vertical physical banner ad for our fried catfish. Photos for the fried catfish will be provided as a reference but we will also accept anything similar to the photo. We will be using the following as our receptacle: https://www.plankoria.example/banner-stand/retractable-banner-stands/
The design must incorporate the following flavor texts:
Fried Catfish
Always Fresh!
Made from Scratch
Hand-cut Fillets
The Best Catfish in Texas
Served with fries, hush puppies, and a 32oz fountain drink
Also available by the pound!
The final design should be creative, professional, and eye-catching for customers.
Updates
Colors
Designer to choose colors to be used in the design.
Requirements
Must have
- We are open to any and all design elements, albeit the 'flavor texts' should not overpower, but complement the fried catfish photo. 'Fried Catfish' can be used in lieu of a main title/logo.
Nice to have
- Transparent or textured backgrounds that can encompass any or all part of the banner such as a cutting board, shadows, abstract, etc to show depth are a plus.
- Use of vectors or objects such as ribbons or shapes to encapsulate the 'flavor texts' are also encouraged.

```html
<!DOCTYPE html>
<html lang="en">
<head>
<meta charset="utf-8">
<title>Fried Catfish Banner</title>
<link href="https://fonts.googleapis.com/css2?family=Bebas+Neue&family=Herr+Von+Muellerhoff&display=swap" rel="stylesheet">
<style>
  :root{
    --page:#ffffff;
    --banner:#000000;
    --yellow:#fff200;
    --white:#ffffff;
    --red:#d3353a;
    --red-dark:#8e1c20;
    --red-light:#e87a7d;
    --wood:#7a5a3a;
    --wood-light:#a88a66;
  }
  html,body{margin:0;padding:0;width:1200px;height:1200px;overflow:hidden;background:var(--page);}
  .canvas{position:relative;width:1200px;height:1200px;}
  .banner{position:absolute;left:353px;top:56px;width:501px;height:1094px;background:var(--banner);overflow:hidden;}
  .food-photo{
    position:absolute;left:0;top:20px;width:501px;height:600px;
    clip-path:polygon(0 33.5%,51% 0,100% 32%,100% 100%,0 100%);
    background:
      radial-gradient(ellipse 55% 20% at 50% 47%,#d9a653 0%,#c48a3c 50%,rgba(196,138,60,0) 80%),
      radial-gradient(ellipse 50% 22% at 50% 48%,#f2f2f2 0%,#e6e6e6 70%,rgba(230,230,230,0) 100%),
      radial-gradient(ellipse 40% 18% at 45% 18%,#c8452a 0%,rgba(200,69,42,0) 80%),
      linear-gradient(180deg,#8a6a48 0%,var(--wood-light) 40%,var(--wood) 70%,#000 100%);
  }
  .title{position:absolute;left:0;width:100%;text-align:center;font-family:'Bebas Neue',sans-serif;line-height:1;margin:0;white-space:nowrap;}
  .title-fried{top:41px;font-size:198px;color:var(--yellow);letter-spacing:-1px;}
  .title-catfish{top:355px;font-size:170px;color:#000;letter-spacing:-1px;}
  .title-reflection{top:355px;font-size:170px;color:#000;letter-spacing:-1px;
    transform:scaleY(-0.4);transform-origin:50% 135px;opacity:.3;}
  .ribbon{position:absolute;left:0;top:535px;width:501px;height:150px;}
  .ribbon-text{
    position:absolute;left:100px;top:577px;width:280px;margin:0;text-align:center;
    font-family:'Bebas Neue',sans-serif;color:var(--white);font-size:35px;line-height:31px;letter-spacing:2px;
    transform:rotate(-8deg);white-space:nowrap;
  }
  .served{position:absolute;left:0;top:710px;width:100%;margin:0;text-align:center;font-family:'Bebas Neue',sans-serif;
    color:var(--yellow);font-size:39px;line-height:36px;letter-spacing:1px;white-space:nowrap;}
  .slogan{position:absolute;left:0;top:0;width:100%;height:0;margin:0;font-family:'Herr Von Muellerhoff',cursive;color:var(--yellow);}
  .slogan span{position:absolute;left:0;width:100%;text-align:center;line-height:1;font-size:92px;white-space:nowrap;}
  .slogan .line-one{top:806px;}
  .slogan .line-two{top:852px;}
  .pound-box{position:absolute;left:59px;top:1000px;width:383px;height:66px;border:2px solid var(--yellow);box-sizing:border-box;
    display:flex;align-items:center;justify-content:center;font-family:'Bebas Neue',sans-serif;color:var(--white);font-size:32px;letter-spacing:1.2px;white-space:nowrap;}
</style>
</head>
<body>
<div class="canvas">
  <div class="banner">
    <div class="food-photo" role="img" aria-label="Plate of cornmeal-fried catfish fillets over fries with a hush puppy and tartar sauce, tomatoes, lemons and onions behind, on a wooden board"></div>
    <h1 class="title title-fried">FRIED</h1>
    <p class="title title-reflection" aria-hidden="true">CATFISH</p>
    <p class="title title-catfish">CATFISH</p>
    <svg class="ribbon" viewBox="0 0 501 150" aria-hidden="true">
      <defs>
        <linearGradient id="ribbonFront" x1="0" x2="1">
          <stop offset="0" stop-color="var(--red)"/>
          <stop offset=".3" stop-color="var(--red-light)"/>
          <stop offset=".6" stop-color="var(--red)"/>
          <stop offset="1" stop-color="#c22a2f"/>
        </linearGradient>
        <linearGradient id="ribbonTail" x1="0" x2="1">
          <stop offset="0" stop-color="var(--red-dark)"/>
          <stop offset=".5" stop-color="var(--red)"/>
          <stop offset="1" stop-color="#b5262b"/>
        </linearGradient>
      </defs>
      <path d="M0 37 L207 0 L212 35 L100 115 L0 132 Z" fill="url(#ribbonTail)"/>
      <path d="M269 35 L476 34 L446 62 L478 98 L270 124 Z" fill="url(#ribbonTail)"/>
      <path d="M207 0 L100 70 L212 35 Z" fill="var(--red-dark)"/>
      <path d="M270 96 L270 124 L335 98 Z" fill="var(--red-dark)"/>
      <path d="M84 60 Q180 24 365 18 L365 84 Q210 92 100 137 Z" fill="url(#ribbonFront)"/>
    </svg>
    <p class="ribbon-text">Always Fresh!<br>Hand-Cut Fillets</p>
    <p class="served">Served with fries, hush puppies,<br>and a 32oz fountain drink</p>
    <p class="slogan"><span class="line-one">The Best</span><span class="line-two">Catfish in Texas</span></p>
    <div class="pound-box">Also available by the pound!</div>
  </div>
</div>
</body>
</html>
```